Stationary for New Company

We need stationary designed for a new company. Details of the required stationary is attached.

The final version should be trendy, clean... only 2 colours (green + grey/black) and professional.

#1: Business Cards (design on 2 sides)
#2: Letterhead (word format)
#3: Cover Page and back cover for proposals
#4: Envelopes,
#5: Thank You card,
#6: Presentation Folder,
#7: Email signatures template (sample attached in word document)

Logo is attached. Logo can be reversed out (will attach once available). Logo can be stacked or horizontal (provided as horizontal).

Files need to be provided in ai + png format.

Target Market(s)

Business owners. More affluent.

Industry/Entity Type

Business

Requirements
Must have
• See brief

Font: Calibri
Should not have
• Photographs / stock photos

```html
<!DOCTYPE html>
<html lang="en">
<head>
<meta charset="utf-8">
<title>Northgate Insurance Brokers – Letterhead Options</title>
<link rel="stylesheet" href="https://fonts.googleapis.com/css2?family=Muli:wght@400&family=Open+Sans:wght@400&family=Arimo:wght@400&display=swap">
<style>
  :root{
    --green:#669c3c;
    --grey:#6d6e70;
    --ink:#1a1a1a;
    --rule:#111111;
    --paper:#ffffff;
    --stage:#ffffff;
    --edge:#d9d9d9;
    --ghost:#e6e6e6;
  }
  *{box-sizing:border-box;margin:0;padding:0}
  html,body{width:1200px;height:800px;overflow:hidden;background:var(--stage)}
  .board{position:relative;width:1200px;height:800px;border:1px solid var(--edge);background:var(--stage);font-family:"Open Sans",sans-serif}
  .sheet{position:absolute;top:8px;width:561px;height:746px;background:var(--paper);overflow:hidden}
  .sheet--wave{left:10px;border:1px solid #eeeeee}
  .sheet--rule{left:613px;border:1px solid var(--edge)}
  .brand{position:absolute;display:flex;align-items:flex-start;gap:12px}
  .brand__mark{width:64px;height:66px;background:var(--green)}
  .brand__name{font-family:"Muli",sans-serif;font-weight:400;color:var(--green);line-height:1}
  .brand__name .line1{display:block;font-size:40px;letter-spacing:-0.5px}
  .brand__name .line2{display:block;font-size:16px;text-align:right;margin-top:2px}
  .sheet--wave .brand{left:146px;top:14px}
  .sheet--rule .brand{left:18px;top:22px}
  .address{position:absolute;font-size:10px;color:var(--ink);line-height:1.3}
  .address--centre{left:0;right:0;top:98px;text-align:center}
  .address--corner{left:419px;top:31px;width:130px}
  .address--corner svg{display:block;margin:0 0 3px 54px;width:20px;height:20px;color:var(--green)}
  .wave{position:absolute;left:0;bottom:0;width:561px;height:86px}
  .ghost-mark{position:absolute;left:217px;top:276px;width:132px;height:141px;background:var(--ghost)}
  .footer-rule{position:absolute;left:15px;top:689px;width:528px;height:3px;background:var(--rule)}
  .contact{position:absolute;display:flex;align-items:center;gap:5px;font-size:10px;white-space:nowrap}
  .contact svg{width:26px;height:26px;flex:none}
  .sheet--wave .contact{top:700px;color:#ffffff}
  .sheet--rule .contact{top:700px;color:var(--ink)}
  .sheet--rule .contact svg{color:var(--green)}
  .caption{position:absolute;top:760px;font-family:"Arimo",sans-serif;font-size:16px;color:var(--ink);width:200px;text-align:center}
</style>
</head>
<body>
<svg width="0" height="0" style="position:absolute" aria-hidden="true">
  <defs>
    <symbol id="ic-phone" viewBox="0 0 26 26">
      <circle cx="13" cy="13" r="12" fill="none" stroke="currentColor" stroke-width="1.6"/>
      <path d="M10.5 7.5c-1.8 1-2 3-1.5 5.5s2 4.5 3.8 5.5c1 .5 2 .3 2.6-.5l-1.8-2.5c-.5.3-1 .3-1.4-.2-.8-1-1.3-2.6-1.3-3.8 0-.6.4-.9.9-1l-.4-3z" fill="currentColor"/>
    </symbol>
    <symbol id="ic-print" viewBox="0 0 26 26">
      <circle cx="13" cy="13" r="12" fill="none" stroke="currentColor" stroke-width="1.6"/>
      <rect x="9" y="6.5" width="8" height="4" fill="none" stroke="currentColor" stroke-width="1.4"/>
      <rect x="6.5" y="10.5" width="13" height="6" rx="1" fill="currentColor"/>
      <rect x="9" y="14.5" width="8" height="5" fill="var(--paper)" stroke="currentColor" stroke-width="1.2"/>
    </symbol>
    <symbol id="ic-headset" viewBox="0 0 26 26">
      <circle cx="13" cy="13" r="12" fill="none" stroke="currentColor" stroke-width="1.6"/>
      <path d="M7.5 14a5.5 5.5 0 0 1 11 0" fill="none" stroke="currentColor" stroke-width="1.6"/>
      <rect x="6.3" y="13" width="2.6" height="4.5" rx="1" fill="currentColor"/>
      <rect x="17.1" y="13" width="2.6" height="4.5" rx="1" fill="currentColor"/>
      <path d="M18.4 17.5c0 1.6-1.5 2.3-3.4 2.3" fill="none" stroke="currentColor" stroke-width="1.2"/>
    </symbol>
    <symbol id="ic-globe" viewBox="0 0 26 26">
      <circle cx="13" cy="13" r="12" fill="none" stroke="currentColor" stroke-width="1.6"/>
      <circle cx="13" cy="13" r="6.5" fill="currentColor"/>
      <path d="M6.5 13h13M13 6.5v13M8 9.5h10M8 16.5h10" stroke="var(--paper)" stroke-width=".8" fill="none"/>
    </symbol>
    <symbol id="ic-home" viewBox="0 0 20 20">
      <circle cx="10" cy="10" r="9" fill="none" stroke="currentColor" stroke-width="1.4"/>
      <path d="M4.5 10.5 10 5.5l5.5 5H14v4.5H6v-4.5z" fill="currentColor"/>
    </symbol>
  </defs>
</svg>

<main class="board">
  <section class="sheet sheet--wave" aria-label="Letterhead with wave footer">
    <div class="brand">
      <div class="brand__mark"></div>
      <div class="brand__name"><span class="line1">Northgate</span><span class="line2">Insurance Brokers</span></div>
    </div>
    <p class="address address--centre">2870 Larch Crescent SW, Calgary, AB&nbsp; T3E 5K2</p>

    <svg class="wave" viewBox="0 0 561 86" preserveAspectRatio="none" aria-hidden="true">
      <path d="M0 22 C160 12 380 16 561 0 V86 H0 Z" fill="var(--green)"/>
    </svg>
    <div class="contact" style="left:18px"><svg><use href="#ic-phone"/></svg>780.555.0142</div>
    <div class="contact" style="left:118px"><svg><use href="#ic-print"/></svg>780.555.0187</div>
    <div class="contact" style="left:227px"><svg><use href="#ic-headset"/></svg>Toll Free 888.555.0199</div>
    <div class="contact" style="left:374px"><svg><use href="#ic-globe"/></svg>www.northgatebrokers.ca</div>
  </section>

  <section class="sheet sheet--rule" aria-label="Letterhead with rule footer">
    <div class="brand">
      <div class="brand__mark"></div>
      <div class="brand__name"><span class="line1">Northgate</span><span class="line2">Insurance Brokers</span></div>
    </div>
    <p class="address address--corner"><svg><use href="#ic-home"/></svg>2870 Larch Crescent SW<br>Calgary, AB&nbsp; T3E 5K2</p>

    <div class="ghost-mark" aria-hidden="true"></div>

    <div class="footer-rule"></div>
    <div class="contact" style="left:18px"><svg><use href="#ic-phone"/></svg>780.555.0142</div>
    <div class="contact" style="left:119px"><svg><use href="#ic-print"/></svg>780.555.0187</div>
    <div class="contact" style="left:227px"><svg><use href="#ic-headset"/></svg>Toll Free 888.555.0199</div>
    <div class="contact" style="left:374px"><svg><use href="#ic-globe"/></svg>www.northgatebrokers.ca</div>
  </section>

  <p class="caption" style="left:188px">Sample a</p>
  <p class="caption" style="left:810px">Sample b</p>
</main>
</body>
</html>
```